Building Certification Company needs a professional letterhead and report template

We are a modern company within an ageing industry. Our industry is responsible for life safety aspects of the built environment, we ensure buildings are safe and fit for occupation.

We use letterhead and reports everyday, we need a smart and professional letterhead that reflects the serious nature of the work we do. We also require a report template of the same ilk.

Target Market(s)

Our target market will consist mainly of professional architects, developers and construction companies.

Industry/Entity Type

Industry

Requirements
Must have
• The letterhead must have:-
Our logo
Our company details, including address, website, email, phone

Address - Suite 208 / 45 Harwick Lane Dunmore NSW 2100

Website - www.quillstonecompliance.example.au

Email - info@qsc.example.au

Phone - 02 5550 3846

The report template must have:-
A title page, which is to incorporate our logo or an aspect of our logo, get creative people.

```html
<!DOCTYPE html>
<html lang="en">
<head>
<meta charset="utf-8">
<title>Quillstone Compliance — Letterhead</title>
<link rel="stylesheet" href="https://fonts.googleapis.com/css2?family=Inter:wght@400;600&display=swap">
<style>
  :root {
    --paper: #ffffff;
    --maroon: #6b2a2a;
    --wine: #8a2c32;
    --wine-dark: #4a1f22;
    --band-grey: #9a9a9a;
    --band-grey-light: #d4d4d4;
    --edge-black: #231816;
    --ink: #1c1c1c;
  }
  * { margin: 0; padding: 0; box-sizing: border-box; }
  html, body { width: 849px; height: 1200px; overflow: hidden; background: var(--paper); }
  .letterhead {
    position: relative;
    width: 849px;
    height: 1200px;
    background: var(--paper);
    font-family: "Inter", Arial, sans-serif;
    color: var(--ink);
    overflow: hidden;
  }
  .header-wave { position: absolute; top: 0; left: 0; width: 849px; height: 180px; display: block; }
  .brand {
    position: absolute;
    top: 186px;
    left: 540px;
    width: 170px;
    text-align: center;
    font-weight: 600;
    color: var(--maroon);
    letter-spacing: 1.5px;
    line-height: 1.15;
  }
  .brand-name { display: block; font-size: 19px; }
  .brand-sub { display: block; font-size: 8.5px; letter-spacing: 1.8px; text-transform: uppercase; }
  .contact-details {
    position: absolute;
    left: 66px;
    top: 1083px;
    font-size: 9px;
    line-height: 13.6px;
    list-style: none;
  }
  .corner-rings {
    position: absolute;
    right: 0;
    bottom: 0;
    width: 180px;
    height: 160px;
    background: radial-gradient(circle at 100% 100%, rgba(30,30,30,0.75) 0%, rgba(90,90,90,0.45) 45%, rgba(160,160,160,0.15) 75%, rgba(255,255,255,0) 100%);
  }
</style>
</head>
<body>
<main class="letterhead">
  <svg class="header-wave" viewBox="0 0 849 180" xmlns="http://www.w3.org/2000/svg" aria-hidden="true">
    <defs>
      <linearGradient id="wineBand" x1="0" y1="0" x2="1" y2="0">
        <stop offset="0" stop-color="var(--wine-dark)"/>
        <stop offset="1" stop-color="var(--wine)"/>
      </linearGradient>
      <linearGradient id="greyBand" x1="0" y1="0" x2="0" y2="1">
        <stop offset="0" stop-color="var(--band-grey-light)"/>
        <stop offset="1" stop-color="var(--band-grey)"/>
      </linearGradient>
      <radialGradient id="ornamentTone" cx="0.3" cy="0.3" r="0.7">
        <stop offset="0" stop-color="#e8e8e8" stop-opacity="0.75"/>
        <stop offset="0.6" stop-color="#b8b8b8" stop-opacity="0.45"/>
        <stop offset="1" stop-color="#ffffff" stop-opacity="0"/>
      </radialGradient>
    </defs>
    <path d="M0 0 H849 V170 C700 142 520 118 320 126 C190 131 90 124 0 110 Z" fill="var(--edge-black)"/>
    <path d="M0 0 H849 V152 C700 120 520 100 320 110 C190 116 90 110 0 98 Z" fill="url(#greyBand)"/>
    <path d="M0 0 H849 V118 C720 72 560 66 400 84 C260 98 120 96 0 82 Z" fill="url(#wineBand)"/>
    <path d="M0 0 H849 V88 C720 46 560 44 400 62 C260 76 120 74 0 62 Z" fill="url(#greyBand)" opacity="0.55"/>
    <path d="M0 0 H849 V70 C720 30 560 28 400 46 C260 60 120 58 0 46 Z" fill="url(#wineBand)"/>
  </svg>
  <svg style="position:absolute;top:0;left:0" width="460" height="135" viewBox="0 0 460 135" role="img" aria-label="Floral flourish over a perforated metal pattern">
    <ellipse cx="200" cy="50" rx="260" ry="85" fill="url(#ornamentTone)"/>
  </svg>

  <div class="brand">
    <span class="brand-name">QUILLSTONE</span>
    <span class="brand-sub">Compliance</span>
  </div>

  <ul class="contact-details">
    <li>Suite 208 / 45 Harwick Lane Dunmore NSW 2100</li>
    <li>www.quillstonecompliance.example.au</li>
    <li>Email - info@qsc.example.au</li>
    <li>Phone - 02 5550 3846</li>
  </ul>

  <div class="corner-rings" role="img" aria-label="Cluster of decorative concentric rings"></div>
</main>
</body>
</html>
```